Hair Salon Brochure

We need a brochure for our hair salon located in Middle Tennessee called Marla Looks of Harbor Bend. Along with standard services, we offer specialized services and accommodations for individuals on the Autism Spectrum, regardless of background or hair type.
At Marla Looks of Harbor Bend, our mission is to create a warm and inclusive haven for individuals of all backgrounds, including those on the autism spectrum and their families. We are dedicated to providing not only exceptional hairstyling services but also hands-on education and specialized cutting techniques for clients with natural textured hair. Our goal is to empower our clients with the knowledge and tools necessary to maintain a successful hair care routine, ensuring they leave our salon feeling confident.
We believe in fostering a sense of community, where parents of younger clients are encouraged to learn the proper hair care techniques for their children, promoting healthy practices at home. Our commitment extends beyond just hair; we are here to help you embrace your true self and recognize the beauty that resides within.
At Marla Looks of Harbor Bend, our passion is to deliver the ultimate client experience, where you can be unapologetically yourself and feel completely at ease. From the moment you step through our doors, you are welcomed not only to discuss your hair concerns but also to engage in meaningful conversations about life. Together, we will collaborate on a personalized plan to achieve your hair goals and transform the way you perceive yourself.
Always remember, when you look good, you feel good, and when you feel good, you can achieve great things. We firmly believe that every individual is 'Beautiful Beyond the Spectrum,' and we are here to celebrate that beauty with you."
https://www.marlalooksbend.net/
Tagline - "Beautiful Beyond the Spectrum"

```html
<!DOCTYPE html>
<html lang="en">
<head>
<meta charset="utf-8">
<title>Marla Looks of Harbor Bend — Beautiful Beyond the Spectrum</title>
<link rel="stylesheet" href="https://fonts.googleapis.com/css2?family=Crimson+Text&family=Open+Sans:wght@400;700&display=swap">
<style>
  :root {
    --orange: #e4712a;
    --blue: #1b68ad;
    --blue-deep: #14579a;
    --blue-light: #3a86c6;
    --paper: #f3f3f2;
    --white: #ffffff;
    --brand-blue: #1d6fb5;
  }
  * { margin: 0; padding: 0; box-sizing: border-box; }
  html, body { width: 848px; height: 1200px; overflow: hidden; background: var(--paper); }
  .brochure {
    position: relative;
    width: 848px;
    height: 1200px;
    overflow: hidden;
    background: var(--paper);
    font-family: "Open Sans", sans-serif;
    color: var(--white);
  }
  .layer { position: absolute; inset: 0; width: 848px; height: 1200px; }
  .brand-name {
    position: absolute;
    left: 61px;
    width: 344px;
    top: 96px;
    text-align: center;
    font-family: "Open Sans", sans-serif;
    font-weight: 400;
    font-size: 22px;
    line-height: 26px;
    color: var(--brand-blue);
  }
  .headline {
    position: absolute;
    left: 94px;
    top: 168px;
    font-weight: 700;
    font-size: 79px;
    line-height: 77px;
    letter-spacing: -1px;
    color: var(--white);
  }
  .tagline {
    position: absolute;
    left: 98px;
    top: 320px;
    font-family: "Crimson Text", serif;
    font-size: 21px;
    color: var(--white);
  }
  .body-copy p {
    position: absolute;
    left: 24px;
    width: 808px;
    font-size: 14.6px;
    line-height: 20.4px;
    color: var(--white);
  }
  .body-copy .mission { top: 596px; }
  .body-copy .community { top: 760px; }
  .body-copy .experience { top: 877px; }
  .body-copy .closing { top: 1018px; }
  .website {
    position: absolute;
    left: 0;
    width: 848px;
    top: 1147px;
    text-align: center;
    font-weight: 700;
    font-size: 20px;
    color: var(--white);
  }
</style>
</head>
<body>
<main class="brochure">
  <svg class="layer" viewBox="0 0 848 1200" aria-hidden="true">
    <defs>
      <linearGradient id="portrait-tones" x1="0" y1="0" x2="1" y2="1">
        <stop offset="0" stop-color="#d9d6d2"/>
        <stop offset="0.45" stop-color="#7a5646"/>
        <stop offset="1" stop-color="#2a2524"/>
      </linearGradient>
      <radialGradient id="wash-tones" cx="0.5" cy="0.45" r="0.7">
        <stop offset="0" stop-color="#3a86c6"/>
        <stop offset="0.6" stop-color="#1f6db1"/>
        <stop offset="1" stop-color="#14579a"/>
      </radialGradient>
    </defs>
  </svg>

  <svg class="layer" viewBox="0 0 848 1200" role="img" aria-label="Photo of a stylist washing a client's hair at the salon basin, tinted blue">
    <polygon points="0,306 848,515 848,1200 0,1200" fill="url(#wash-tones)"/>
  </svg>

  <svg class="layer" viewBox="0 0 848 1200" role="img" aria-label="Portrait photo of the salon owner smiling">
    <polygon points="405,0 848,0 848,515 405,406" fill="url(#portrait-tones)"/>
  </svg>

  <svg class="layer" viewBox="0 0 848 1200" aria-hidden="true">
    <polygon class="title-panel" points="61,0 405,0 405,528 61,444" fill="var(--orange)"/>
  </svg>

  <header>
    <p class="brand-name">Marla Looks<br>of Harbor Bend</p>
    <h1 class="headline">MARLA<br>LOOKS</h1>
    <p class="tagline">Beautiful Beyond the Spectrum</p>
  </header>

  <section class="body-copy">
    <p class="mission">At Marla Looks of Harbor Bend, our mission is to create a warm and inclusive haven for individuals of all backgrounds, including those on the autism spectrum and their families. We are dedicated to providing not only exceptional hairstyling services but also hands-on education and specialized cutting techniques for clients with natural textured hair. Our goal is To empower our clients with the knowledge and tools necessary to maintain a successful hair care routine, ensuring they leave our salon feeling confident.</p>
    <p class="community">We believe in fostering a sense of community, where parents of younger clients are encouraged to learn the proper hair care techniques for their children, promoting healthy practices at home. Our commitment extends beyond just hair; we are here to help you embrace your true self and recognize the beauty that resides within.</p>
    <p class="experience">At Marla Looks of Harbor Bend, our passion is to deliver the ultimate client experience, where you can be unapologetically yourself and feel completely at ease. From the moment you step through our doors, you are welcomed not only to discuss your hair concerns but also to engage in meaningful conversations about life. Together, we will collaborate on a personalized plan to achieve your hair goals and transform the way you perceive yourself.</p>
    <p class="closing">Always remember, when you look good, you feel good, and when you feel good, you can achieve great things. We firmly believe that every individual is 'Beautiful Beyond the Spectrum,' and we are here to celebrate that beauty with you."</p>
  </section>

  <footer class="website">www.marlalooksbend.net</footer>
</main>
</body>
</html>
```